Solar appointment reminder card

We are looking for a new design for our appointment reminder card since we have changed our logo. The card should have the new logo along with space for the employee to hand write the customers appointment date, time, the employees name and phone number.
I've uploaded what our old basic appointment card looked like and our new logo.

The cards should be in a standard business card size and could be horizontal or vertical.

```html
<!DOCTYPE html>
<html lang="en">
<head>
<meta charset="utf-8">
<title>Appointment Reminder Card</title>
<link rel="stylesheet" href="https://fonts.googleapis.com/css2?family=Arimo:wght@700&display=swap">
<style>
  :root {
    --page-bg: #eeeeee;
    --card-bg: #ffffff;
    --ink: #111111;
    --reminder-red: #e8141b;
    --brand-orange: #f7901e;
    --sun-yellow: #fdd20a;
    --ring-yellow: #fbe20c;
    --ring-orange: #f7a21b;
    --swoosh-red: #ee3e23;
  }
  html, body {
    margin: 0;
    width: 1200px;
    height: 1200px;
    overflow: hidden;
    background: var(--page-bg);
    font-family: "Arimo", Arial, sans-serif;
  }
  .reminder-card {
    position: absolute;
    left: 145px;
    top: 328px;
    width: 910px;
    height: 544px;
    background: var(--card-bg);
    overflow: hidden;
  }
  .card-art {
    position: absolute;
    inset: 0;
  }
  .brand {
    position: absolute;
    left: 62px;
    top: 108px;
    display: flex;
    align-items: center;
    gap: 16px;
  }
  .brand-dot {
    width: 66px;
    height: 66px;
    border-radius: 50%;
    background: var(--sun-yellow);
    flex: none;
  }
  .brand-name {
    color: var(--brand-orange);
    font-weight: 700;
    font-size: 34px;
    letter-spacing: 0.5px;
    line-height: 38px;
    white-space: nowrap;
  }
  .reminder-title {
    position: absolute;
    left: 548px;
    top: 96px;
    width: 310px;
    text-align: center;
    color: var(--reminder-red);
    font-weight: 700;
    font-size: 37px;
    line-height: 42px;
    margin: 0;
  }
  .field-label {
    position: absolute;
    color: var(--ink);
    font-weight: 700;
    margin: 0;
    line-height: 1;
    white-space: nowrap;
  }
  .label-date { left: 244px; width: 418px; text-align: center; top: 266px; font-size: 34px; }
  .label-time { left: 70px; top: 388px; font-size: 28px; }
  .label-rep { left: 288px; width: 318px; text-align: center; top: 384px; font-size: 28px; }
  .label-phone { left: 718px; top: 388px; font-size: 28px; }
  .write-line {
    position: absolute;
    height: 3px;
    background: var(--ink);
  }
  .line-date { left: 244px; width: 418px; top: 359px; }
  .line-time { left: 60px; width: 184px; top: 474px; }
  .line-rep { left: 288px; width: 318px; top: 477px; }
  .line-phone { left: 646px; width: 200px; top: 478px; }
</style>
</head>
<body>
  <main class="reminder-card">
    <svg class="card-art" width="910" height="544" viewBox="0 0 910 544" aria-hidden="true">
      <defs>
        <linearGradient id="swoosh-fill" x1="0" y1="0" x2="1" y2="0">
          <stop offset="0" stop-color="var(--ring-yellow)"/>
          <stop offset="0.5" stop-color="var(--ring-orange)"/>
          <stop offset="1" stop-color="var(--swoosh-red)"/>
        </linearGradient>
        <linearGradient id="ring-outer" x1="0" y1="0" x2="1" y2="1">
          <stop offset="0" stop-color="var(--ring-yellow)"/>
          <stop offset="1" stop-color="var(--ring-orange)"/>
        </linearGradient>
        <linearGradient id="ring-inner" x1="0" y1="0" x2="1" y2="1">
          <stop offset="0" stop-color="var(--ring-orange)"/>
          <stop offset="1" stop-color="var(--swoosh-red)"/>
        </linearGradient>
      </defs>
      <circle class="ring-back" cx="712" cy="118" r="222" fill="url(#ring-outer)"/>
      <circle class="ring-mid" cx="724" cy="128" r="200" fill="url(#ring-inner)"/>
      <circle class="ring-face" cx="722" cy="134" r="176" fill="var(--card-bg)"/>
      <rect class="lower-panel" x="0" y="300" width="910" height="244" fill="var(--card-bg)"/>
      <path class="swoosh" d="M0 300 Q 470 140 910 282 L 910 304 Q 470 180 0 340 Z" fill="url(#swoosh-fill)"/>
      <path class="swoosh-cover" d="M0 340 Q 470 180 910 304 L 910 544 L 0 544 Z" fill="var(--card-bg)"/>
    </svg>

    <div class="brand">
      <span class="brand-dot"></span>
      <span class="brand-name">BRIGHT RIDGE<br>SOLAR</span>
    </div>

    <h1 class="reminder-title">APPOINTMENT<br>REMINDER</h1>

    <p class="field-label label-date">APPOINTMENT DATE</p>
    <span class="write-line line-date"></span>

    <p class="field-label label-time">TIME</p>
    <p class="field-label label-rep">REPRESENTATIVE</p>
    <p class="field-label label-phone">PHONE</p>
    <span class="write-line line-time"></span>
    <span class="write-line line-rep"></span>
    <span class="write-line line-phone"></span>
  </main>
</body>
</html>
```